Landing Page and Logo for Auto-Blogging Platform

I created a platform that allows users to start a blog for their business, hobby, charity, etc. I need a landing page where users can learn about the platform, benefits of consistent blogging, SEO value, plans/pricing, etc. The landing page needs to have multiple call to action buttons encouraging the visitor to register/sign up for a free trial.

In addition to the landing page, I need a page for users to establish the settings for their blog. This page should be a fairly simple form, intended for the user to enter a few details to set up their blog:
1. Name of Blog
2. Up to 10 topics and/or keywords the blog should focus on
3. Theme: Color-scheme and logo upload for blog.

I have attached the specifications of the platform's functionality so you can better understand how it works, plans/pricing, etc.

I also need a logo for the business. The name of the platform is PostNook.

Target Market(s)

Website owners, bloggers, business owners

Industry/Entity Type

Technology, Internet, web design

Coding

Coded - Design and coding required

Number of Pages Required

2 page

Colors
0054AA
0677BA
7BADD7
CADEEF
E8F1F8
0094D4
00A9DD
6FCCEA
C7EBF8
E9F6FB

Requirements
Must have
• Eye-catching design but fairly light on content (keep it simple and brief.)
Nice to have
• Eye-catching yet simple design, clean and easy to understand what we are offering.
Should not have
• Too much “wordy” and confusing content.

```html
<!DOCTYPE html>
<html lang="en">
<head>
<meta charset="utf-8">
<title>PostNook – Set Up Your Blog</title>
<link href="https://fonts.googleapis.com/css2?family=Poppins:wght@400;500;600;700&family=Nunito:wght@400;500;600&display=swap" rel="stylesheet">
<style>
:root{
  --navy-top:#0a1230;
  --navy-mid:#0d1f5a;
  --navy-low:#10307e;
  --brand-blue:#1a73f0;
  --btn-blue:#0a63f0;
  --cta-blue:#0b6cf5;
  --cyan:#00c4dd;
  --green:#4caf50;
  --card:#e8f1fc;
  --step-active:#5b55d6;
  --step-muted:#a8a6e8;
  --ink:#2b2f3a;
  --muted:#9aa3b5;
  --band:#a8b9dc;
  --white:#ffffff;
}
*{box-sizing:border-box;margin:0;padding:0}
html,body{width:1200px;height:876px;overflow:hidden;background:var(--white);font-family:'Poppins',sans-serif}
.page{position:relative;width:1200px;height:876px;overflow:hidden}
.hero-bg{position:absolute;inset:0;width:1200px;height:400px}
.header{position:absolute;top:0;left:0;width:1200px;height:76px}
.brand{position:absolute;left:173px;top:22px;display:flex;align-items:center;gap:9px;color:#4b8cff;font-weight:700;font-size:25px;letter-spacing:-.3px}
.brand-dot{width:22px;height:22px;border-radius:50%;background:#4b8cff}
.nav{position:absolute;top:28px;left:458px;display:flex;gap:26px;color:var(--white);font-weight:500;font-size:12.5px}
.btn-cta{position:absolute;left:802px;top:23px;width:109px;height:31px;border-radius:16px;background:var(--cta-blue);color:#fff;font-size:12px;font-weight:500;display:flex;align-items:center;justify-content:center}
.btn-outline{position:absolute;left:942px;top:23px;width:93px;height:31px;border-radius:16px;border:1px solid #fff;color:#fff;font-size:12px;font-weight:500;display:flex;align-items:center;justify-content:center}
.hero-text{position:absolute;top:104px;left:0;width:1200px;text-align:center;color:#fff}
.eyebrow{font-size:16px;font-weight:500;letter-spacing:-.2px}
.title{margin-top:18px;font-size:35px;font-weight:700;line-height:42px;letter-spacing:-.5px}
.title span{display:block;color:var(--brand-blue)}
.card{position:absolute;left:155px;top:296px;width:891px;height:395px;background:var(--card);border-radius:8px;font-family:'Nunito',sans-serif}
.step{position:absolute;top:43px;height:52px;border:1px solid #c4c8e0;display:flex;flex-direction:column;align-items:center;justify-content:center;gap:4px;font-size:11.5px;color:var(--muted)}
.step .num{width:15px;height:15px;background:var(--step-muted);color:#fff;font-size:9px;display:flex;align-items:center;justify-content:center}
.step.active{border-color:#5c6070;color:#4a4f5c}
.step.active .num{background:var(--step-active)}
.step-line{position:absolute;top:58px;height:1px;background:#cfd6e6}
.lead{position:absolute;top:110px;left:0;width:100%;text-align:center;font-size:12.5px;color:var(--ink)}
.tabs{position:absolute;top:134px;left:276px;display:flex;gap:8px}
.tab{height:34px;padding:0 15px;display:flex;align-items:center;font-size:12.5px;color:#5565d6;background:#eef0f5}
.tab.on{background:var(--green);color:#fff}
.prompt{position:absolute;top:186px;left:0;width:100%;text-align:center;font-size:12.5px;color:var(--ink)}
.field{position:absolute;left:250px;top:210px;width:390px;height:36px;background:#fff;border:1px solid #b9bec9;border-radius:2px;padding-left:8px;display:flex;align-items:center;font-size:12.5px;color:#6d7380}
.generate{position:absolute;left:250px;top:254px;width:390px;height:34px;background:var(--green);color:#fff;font-size:12.5px;display:flex;align-items:center;justify-content:center;border-radius:2px}
.btn-prev,.btn-next{position:absolute;top:307px;width:117px;height:30px;display:flex;align-items:center;justify-content:center;color:#fff;font-size:12px;font-family:'Poppins',sans-serif;border-radius:2px}
.btn-prev{left:39px;background:var(--cyan)}
.btn-next{left:734px;background:var(--btn-blue)}
.footer{position:absolute;left:0;top:777px;width:1200px;height:99px;background:linear-gradient(180deg,#0a1028 0%,#0c1c52 100%)}
.footer-rule{position:absolute;left:155px;top:40px;width:891px;height:1px;background:#233066}
.copy{position:absolute;left:170px;top:61px;color:#c8cee0;font-size:11px}
.social{position:absolute;top:56px;width:27px;height:28px;border:1px solid #fff;border-radius:3px}
.to-top{position:absolute;left:1143px;top:819px;width:34px;height:34px;border-radius:50%;background:var(--cta-blue)}
</style>
</head>
<body>
<div class="page">
  <svg class="hero-bg" viewBox="0 0 1200 400" aria-hidden="true">
    <defs>
      <linearGradient id="heroGrad" x1="0" y1="0" x2="0" y2="1">
        <stop offset="0" stop-color="#0a1230"/>
        <stop offset=".55" stop-color="#0d1f5a"/>
        <stop offset="1" stop-color="#10307e"/>
      </linearGradient>
    </defs>
    <path d="M1046 320 L1200 316 L1200 376 L1046 370 Z" fill="#a8b9dc"/>
    <path d="M0 0 H1200 V344 L1046 345 V300 H155 V348 L0 344 Z" fill="url(#heroGrad)"/>
  </svg>

  <header class="header">
    <div class="brand"><span class="brand-dot"></span>PostNook</div>
    <nav class="nav"><span>Features</span><span>Pricing</span><span>Help</span><span>Contact</span></nav>
    <div class="btn-cta">Start Your Blog</div>
    <div class="btn-outline">Contact Us</div>
  </header>

  <section class="hero-text">
    <p class="eyebrow">Start Your Blog in Minutes with PostNook</p>
    <h1 class="title">Set Up Your Blog<span>in Three Simple Steps</span></h1>
  </section>

  <section class="card">
    <div class="step" style="left:39px;width:80px"><span class="num">1</span>Blog Details</div>
    <div class="step-line" style="left:124px;width:362px"></div>
    <div class="step active" style="left:336px;width:162px"><span class="num">2</span>Choose Topics &amp; Keywords</div>
    <div class="step-line" style="left:504px;width:362px"></div>
    <div class="step" style="left:715px;width:136px"><span class="num">3</span>Design Customization</div>

    <p class="lead">Define the content focus by choosing your blog’s topics and keywords.</p>
    <div class="tabs">
      <span class="tab">Manual Entry</span>
      <span class="tab">Upload CSV</span>
      <span class="tab on">Generate with AI</span>
    </div>
    <p class="prompt">Describe your blog, and we'll generate topics for you:</p>
    <div class="field">e.g., Generate 10 blog topics for a travel blog...</div>
    <div class="generate">Generate Topics</div>
    <div class="btn-prev">Previous</div>
    <div class="btn-next">Next</div>
  </section>

  <footer class="footer">
    <div class="footer-rule"></div>
    <p class="copy">© 2024 PostNook</p>
    <span class="social" style="left:935px"></span>
    <span class="social" style="left:969px"></span>
    <span class="social" style="left:1002px"></span>
  </footer>

  <div class="to-top">
    <svg width="34" height="34" viewBox="0 0 34 34" aria-hidden="true"><path d="M12 19 L17 14 L22 19" fill="none" stroke="#fff" stroke-width="2.2" stroke-linecap="round" stroke-linejoin="round"/></svg>
  </div>
</div>
</body>
</html>
```